Luxury Inclusive Beauty Brand Needs Labels & Boxes for Product Line

We need updated labels and boxes for our cosmetic and skin care line. Our company is BRISA + KO. and we focus on providing upscale, natural and organic beauty products inclusive of diverse and deeper skin tones for women of color, especially black women. We have a seven piece skin care collection called DERMAVA Tamarind Collection and a mineral make-up line consisting of eight products. The design of all products should be the same with just dimensions and title/ingredient list differences. We would like to see designs that use our coral color e85350, work well on black packaging (bottles, lipstick tubes etc.) and include white and other additional pretty colors, metallics or patterns representative of ethnic (AFRICAN), bohemian or tribal influence. The final design should communicate luxury, floral/fauna environmentalism, and afrocentric culture influences.
We have included files of various prints we like and the type of lifestyle our customer aspires to/is attracted to. We have included in the files below some examples of packaging we like but we want something original to capture the attention of our target market, upper income health and ethnic conscious black women age 30 - 55 who love natural and organic products. The names of our products include the list below however if design can be submitted showing design on 1 tall box and 1 short box and 1 lipstick size box that would be great:
DERMAVA Tamarind Collection Cleansing Oil (dropper)
DERMAVA Tamarind Collection Balancing Toner (tall spray bottle)
DERMAVA Tamarind Collection Moisturizing Serum (dropper)
DERMAVA Tamarind Collection Moisturizing Cream (short box jar)
DERMAVA Tamarind Lip Scrub (short box - jar)
Luminous Mineral Foundation (short box- jar)
CC Cream
Moisturizing Lip Stick (lipstick box)
WINKORA Natural Mascara
Pimsy Tamsy Lip Crayon
Gel Eye Liner
Organic Make-up Remover (tall spray bottle)
Face & Eye Primer
Final dimensions /dies of boxes can be sent to winner of design competition.
women of color, age 30-55, income 50 - 150K, natural hair and organic lifestyle, yoga
Cosmetics
- label and box
- include the color e85350
- include logo
- easy way to differentiate skincare from make-up products

```html
<!DOCTYPE html>
<html lang="en">
<head>
<meta charset="utf-8">
<title>BRISA + KO. Cleansing Oil Label</title>
<link rel="stylesheet" href="https://fonts.googleapis.com/css2?family=Montserrat:wght@400&family=Kaushan+Script&display=swap">
<style>
  :root {
    --page: #ffffff;
    --label-deep: #9c2226;
    --label-mid: #c23a3a;
    --label-coral: #e85350;
    --label-glow: #f0665f;
    --ink-light: #ffffff;
    --ink-soft: #f6dcd8;
  }
  * { margin: 0; padding: 0; box-sizing: border-box; }
  html, body {
    width: 1070px;
    height: 1200px;
    overflow: hidden;
    background: var(--page);
  }
  .canvas {
    position: relative;
    width: 1070px;
    height: 1200px;
  }
  .label {
    position: absolute;
    left: 205px;
    top: 60px;
    width: 660px;
    height: 1080px;
    overflow: hidden;
  }
  .label__botanicals {
    position: absolute;
    inset: 0;
    background:
      radial-gradient(ellipse 60% 30% at 30% 45%, rgba(232, 83, 80, 0.55), transparent 70%),
      radial-gradient(ellipse 50% 25% at 75% 30%, rgba(232, 83, 80, 0.4), transparent 70%),
      radial-gradient(ellipse 70% 30% at 50% 85%, var(--label-glow), transparent 75%),
      linear-gradient(180deg,
        var(--label-deep) 0%,
        var(--label-mid) 35%,
        var(--label-coral) 62%,
        var(--label-coral) 100%);
  }
  .brand {
    position: absolute;
    top: 92px;
    left: 0;
    width: 100%;
    display: flex;
    flex-direction: column;
    align-items: center;
    gap: 22px;
  }
  .brand__mark {
    width: 54px;
    height: 54px;
    border: 3px solid var(--ink-soft);
    border-radius: 50%;
  }
  .brand__name {
    font-family: "Montserrat", sans-serif;
    font-weight: 400;
    font-size: 40px;
    letter-spacing: 1px;
    color: var(--ink-soft);
  }
  .product-title {
    position: absolute;
    left: 30px;
    right: 30px;
    top: 520px;
    text-align: center;
    font-family: "Kaushan Script", cursive;
    font-weight: 400;
    color: var(--ink-light);
    line-height: 1;
    white-space: nowrap;
  }
  .product-title__line {
    display: block;
    font-size: 124px;
    transform: rotate(-5deg);
  }
  .product-title__line--second {
    margin-top: 30px;
    margin-left: 30px;
    font-size: 150px;
  }
</style>
</head>
<body>
  <main class="canvas">
    <section class="label">
      <div class="label__botanicals" role="img" aria-label="Silhouette pattern of wildflowers, leaves and grasses in coral tones on deep red"></div>
      <header class="brand">
        <span class="brand__mark" aria-hidden="true"></span>
        <span class="brand__name">BRISA + KO.</span>
      </header>
      <h1 class="product-title">
        <span class="product-title__line">Cleansing</span>
        <span class="product-title__line product-title__line--second">Oil</span>
      </h1>
    </section>
  </main>
</body>
</html>
```